BEACON CABS

Taxi card design

Need changes very slow in replying to my messages.

Target Market(s)

Customers

Industry/Entity Type

Taxi

Contact Information for Business Card

See previous design

Font styles to use
Sans Serif

Colors
A7469A
B969AE
D3A5CF
EDDBEB
F8F0F9
6B429C
8869AF
B7A5CE
E3DAEB
F3F0F8

Requirements
Nice to have
• We are in the business of looking after people, not just driving vehicles front
Should not have
• Front number 01632 480 480 needs to big big

```html
<!DOCTYPE html>
<html lang="en">
<head>
<meta charset="utf-8">
<title>Beacon Cabs – Business Card</title>
<link rel="stylesheet" href="https://fonts.googleapis.com/css2?family=Exo+2:wght@400;600;700;800&family=Montserrat:wght@400;500;700&display=swap">
<style>
  :root {
    --bg: #d9d9db;
    --paper: #ffffff;
    --ink: #141414;
    --grey-text: #6e6e6e;
    --purple: #8a1f8c;
    --purple-deep: #4e1570;
    --purple-mid: #7a1c86;
    --purple-glow: #9a2596;
    --band: #141414;
    --silver: #d4d2d6;
    --white: #ffffff;
  }
  * { box-sizing: border-box; margin: 0; padding: 0; }
  html, body { width: 1200px; height: 800px; overflow: hidden; }
  body {
    background: var(--bg);
    font-family: "Montserrat", sans-serif;
    position: relative;
  }
  .card {
    position: absolute;
    top: 245px;
    width: 540px;
    height: 310px;
    border-radius: 18px;
    overflow: hidden;
    box-shadow: 0 6px 18px rgba(0,0,0,0.18);
  }
  /* ---------- Front (white) ---------- */
  .card-front { left: 40px; background: var(--paper); }
  .brand-block {
    position: absolute;
    right: 34px;
    top: 38px;
    text-align: right;
  }
  .brand-name {
    font-family: "Exo 2", sans-serif;
    font-weight: 800;
    font-size: 36px;
    letter-spacing: 0.5px;
    color: var(--purple);
    line-height: 1;
  }
  .brand-phone {
    margin-top: 10px;
    font-family: "Exo 2", sans-serif;
    font-weight: 600;
    font-size: 27px;
    color: var(--ink);
    display: flex;
    align-items: center;
    justify-content: flex-end;
    gap: 8px;
    line-height: 1;
  }
  .brand-phone svg { width: 20px; height: 20px; fill: var(--purple); }
  .divider {
    position: absolute;
    left: 30px;
    right: 34px;
    top: 150px;
    height: 1px;
    background: var(--ink);
  }
  .services {
    position: absolute;
    left: 30px;
    top: 90px;
    list-style: none;
    font-family: "Exo 2", sans-serif;
    font-weight: 700;
    font-size: 16px;
    line-height: 19px;
    color: var(--purple);
    text-transform: uppercase;
  }
  .address {
    position: absolute;
    left: 30px;
    top: 164px;
    font-style: normal;
    font-size: 13px;
    line-height: 17px;
    color: var(--grey-text);
  }
  .contacts {
    position: absolute;
    right: 34px;
    top: 162px;
    list-style: none;
    font-size: 12.5px;
    line-height: 17px;
    color: var(--ink);
    text-align: right;
  }
  .contacts li { display: flex; align-items: center; justify-content: flex-end; gap: 6px; }
  .contacts svg { width: 11px; height: 11px; fill: var(--purple); }
  .phone-band { position: absolute; left: 0; bottom: 0; width: 540px; height: 90px; }
  .band-numbers {
    position: absolute;
    left: 22px;
    right: 22px;
    bottom: 16px;
    display: flex;
    justify-content: space-between;
    list-style: none;
    font-family: "Exo 2", sans-serif;
    font-weight: 700;
    font-size: 15px;
    color: var(--white);
  }
  .band-numbers li { display: flex; align-items: center; gap: 4px; }
  .band-numbers svg { width: 11px; height: 11px; fill: var(--purple-glow); }
  /* ---------- Back (purple) ---------- */
  .card-back {
    left: 620px;
    background: radial-gradient(ellipse at 48% 52%, var(--purple-glow) 0%, var(--purple-mid) 45%, var(--purple-deep) 100%);
  }
  .back-brand {
    position: absolute;
    left: 0; right: 0;
    top: 100px;
    text-align: center;
    font-family: "Exo 2", sans-serif;
    font-weight: 800;
    font-size: 56px;
    letter-spacing: 1px;
    color: var(--ink);
    line-height: 1;
  }
  .back-phone {
    position: absolute;
    left: 0; right: 0;
    top: 186px;
    display: flex;
    align-items: center;
    justify-content: center;
    gap: 10px;
    font-family: "Exo 2", sans-serif;
    font-weight: 600;
    font-size: 34px;
    color: var(--silver);
    line-height: 1;
  }
  .back-phone svg { width: 24px; height: 24px; fill: var(--ink); }
</style>
</head>
<body>

<section class="card card-front" aria-label="Business card front">
  <div class="brand-block">
    <div class="brand-name">BEACON CABS</div>
    <div class="brand-phone">
      <svg viewBox="0 0 24 24" aria-hidden="true"><path d="M6.6 10.8a15.1 15.1 0 0 0 6.6 6.6l2.2-2.2c.3-.3.7-.4 1-.2 1.1.4 2.3.6 3.6.6.6 0 1 .4 1 1V20c0 .6-.4 1-1 1A17 17 0 0 1 3 4c0-.6.4-1 1-1h3.5c.6 0 1 .4 1 1 0 1.3.2 2.5.6 3.6.1.3 0 .7-.2 1z"/></svg>
      01632 480 480
    </div>
  </div>

  <ul class="services">
    <li>Airport Transfers</li>
    <li>Minibuses</li>
    <li>School Transport</li>
  </ul>

  <div class="divider"></div>

  <address class="address">
    Old Chapel Hall<br>
    Market Row, Elmbridge<br>
    EB4 7QT
  </address>

  <ul class="contacts">
    <li>Free Ph: 0800 000 0 123
      <svg viewBox="0 0 24 24" aria-hidden="true"><path d="M6.6 10.8a15.1 15.1 0 0 0 6.6 6.6l2.2-2.2c.3-.3.7-.4 1-.2 1.1.4 2.3.6 3.6.6.6 0 1 .4 1 1V20c0 .6-.4 1-1 1A17 17 0 0 1 3 4c0-.6.4-1 1-1h3.5c.6 0 1 .4 1 1 0 1.3.2 2.5.6 3.6.1.3 0 .7-.2 1z"/></svg>
    </li>
    <li>bookings@beaconcabs.co.uk
      <svg viewBox="0 0 24 24" aria-hidden="true"><rect x="2" y="5" width="20" height="14" rx="1"/></svg>
    </li>
    <li>www.beaconcabs.co.uk
      <svg viewBox="0 0 24 24" aria-hidden="true"><circle cx="12" cy="12" r="10"/></svg>
    </li>
  </ul>

  <svg class="phone-band" viewBox="0 0 540 90" preserveAspectRatio="none" aria-hidden="true">
    <path fill="var(--purple)" d="M0 38 L540 22 L540 90 L0 90 Z"/>
    <path fill="var(--band)" d="M0 46 L540 30 L540 90 L0 90 Z"/>
  </svg>
  <ul class="band-numbers">
    <li><svg viewBox="0 0 24 24" aria-hidden="true"><path d="M6.6 10.8a15.1 15.1 0 0 0 6.6 6.6l2.2-2.2c.3-.3.7-.4 1-.2 1.1.4 2.3.6 3.6.6.6 0 1 .4 1 1V20c0 .6-.4 1-1 1A17 17 0 0 1 3 4c0-.6.4-1 1-1h3.5c.6 0 1 .4 1 1 0 1.3.2 2.5.6 3.6.1.3 0 .7-.2 1z"/></svg>01632 48 66 66</li>
    <li><svg viewBox="0 0 24 24" aria-hidden="true"><path d="M6.6 10.8a15.1 15.1 0 0 0 6.6 6.6l2.2-2.2c.3-.3.7-.4 1-.2 1.1.4 2.3.6 3.6.6.6 0 1 .4 1 1V20c0 .6-.4 1-1 1A17 17 0 0 1 3 4c0-.6.4-1 1-1h3.5c.6 0 1 .4 1 1 0 1.3.2 2.5.6 3.6.1.3 0 .7-.2 1z"/></svg>01632 20 20 20</li>
    <li><svg viewBox="0 0 24 24" aria-hidden="true"><path d="M6.6 10.8a15.1 15.1 0 0 0 6.6 6.6l2.2-2.2c.3-.3.7-.4 1-.2 1.1.4 2.3.6 3.6.6.6 0 1 .4 1 1V20c0 .6-.4 1-1 1A17 17 0 0 1 3 4c0-.6.4-1 1-1h3.5c.6 0 1 .4 1 1 0 1.3.2 2.5.6 3.6.1.3 0 .7-.2 1z"/></svg>01632 48 88 11</li>
  </ul>
</section>

<section class="card card-back" aria-label="Business card back">
  <div class="back-brand">BEACON CABS</div>
  <div class="back-phone">
    <svg viewBox="0 0 24 24" aria-hidden="true"><path d="M6.6 10.8a15.1 15.1 0 0 0 6.6 6.6l2.2-2.2c.3-.3.7-.4 1-.2 1.1.4 2.3.6 3.6.6.6 0 1 .4 1 1V20c0 .6-.4 1-1 1A17 17 0 0 1 3 4c0-.6.4-1 1-1h3.5c.6 0 1 .4 1 1 0 1.3.2 2.5.6 3.6.1.3 0 .7-.2 1z"/></svg>
    01632 480 480
  </div>
</section>

</body>
</html>
```